Australian Civil Construction, Quarry & Mining Services needs a business card

We need a business card designed for our Civil Construction, Quarry & Mining Services based in the country in Australia.
Our Company Brackley Earthworks provide innovate solutions for infrastructure, agricultural and mining (aggregate, sand, roadbase) industry.
We would like our business cards to be double sided
Front of card: black background or something that resembles our business colours. (it doesn't have to be black we are open to options)
- Company name - Brackley Earthworks
- Either our logo or some sort of icon/picture that resembles our business
- Website - https://brackleyearthworks.com.au/
- We will have a number of different names, positions descriptions, phone numbers and emails on separate cards for each of our managers/directors

```html
<!DOCTYPE html>
<html lang="en">
<head>
<meta charset="utf-8">
<title>Brackley Earthworks – Business Card</title>
<link rel="stylesheet" href="https://fonts.googleapis.com/css2?family=Open+Sans:wght@400;700;800&display=swap">
<style>
  :root {
    --clay: #d4722f;
    --coal: #000000;
    --ink: #111111;
    --paper: #ffffff;
    --card-w: 700px;
    --card-h: 400px;
  }
  * { margin: 0; padding: 0; box-sizing: border-box; }
  html, body {
    width: 1200px;
    height: 2400px;
    overflow: hidden;
    background: var(--paper);
    font-family: "Open Sans", sans-serif;
  }
  .sheet { position: relative; width: 1200px; height: 2400px; }
  .card {
    position: absolute;
    width: var(--card-w);
    height: var(--card-h);
    background: var(--clay);
    overflow: hidden;
    box-shadow: 10px 14px 22px rgba(0,0,0,0.35);
  }
  .card-front { left: 150px; top: 757px; }
  .card-back  { left: 410px; top: 1242px; }
  .card-curve { position: absolute; inset: 0; width: 100%; height: 100%; }

  .front-mark {
    position: absolute;
    left: 340px; top: 60px;
    width: 160px; height: 160px;
    border-radius: 50%;
    background: var(--ink);
  }
  .front-name {
    position: absolute;
    left: 250px; right: 0; top: 330px;
    text-align: center;
    font-weight: 800;
    font-size: 24px;
    letter-spacing: 0.3px;
    color: var(--ink);
    text-transform: uppercase;
  }

  .back-mark {
    position: absolute;
    left: 22px; top: 160px;
    width: 220px;
    display: flex; align-items: center; gap: 10px;
    color: var(--clay);
    font-weight: 700;
    font-size: 19px;
    line-height: 1.15;
  }
  .back-mark .dot {
    flex: none;
    width: 34px; height: 34px;
    border-radius: 50%;
    background: var(--clay);
  }
  .back-details {
    position: absolute;
    right: 26px; top: 42px;
    text-align: right;
    color: var(--ink);
  }
  .company { font-weight: 800; font-size: 29px; line-height: 1.2; text-transform: uppercase; }
  .person { margin-top: 12px; font-weight: 800; font-size: 26px; line-height: 1.15; }
  .role { font-size: 21px; line-height: 1.25; }
  .address { margin-top: 28px; font-size: 21px; line-height: 27px; }
  .address strong { font-weight: 700; }
  .web { margin-top: 25px; font-size: 21px; line-height: 27px; }
</style>
</head>
<body>
<main class="sheet">

  <section class="card card-front" aria-label="Card front">
    <svg class="card-curve" viewBox="0 0 700 400" preserveAspectRatio="none" aria-hidden="true">
      <defs>
        <filter id="curve-shadow-front" x="-10%" y="-10%" width="130%" height="130%">
          <feDropShadow dx="6" dy="0" stdDeviation="6" flood-color="#000" flood-opacity="0.45"/>
        </filter>
      </defs>
      <path d="M0 0 H245 Q300 200 245 400 H0 Z" fill="var(--coal)" filter="url(#curve-shadow-front)"/>
    </svg>
    <div class="front-mark" aria-hidden="true"></div>
    <p class="front-name">Brackley Earthworks</p>
  </section>

  <section class="card card-back" aria-label="Card back">
    <svg class="card-curve" viewBox="0 0 700 400" preserveAspectRatio="none" aria-hidden="true">
      <defs>
        <filter id="curve-shadow-back" x="-10%" y="-10%" width="130%" height="130%">
          <feDropShadow dx="6" dy="0" stdDeviation="6" flood-color="#000" flood-opacity="0.45"/>
        </filter>
      </defs>
      <path d="M0 0 H245 Q310 200 245 400 H0 Z" fill="var(--coal)" filter="url(#curve-shadow-back)"/>
    </svg>
    <div class="back-mark">
      <span class="dot" aria-hidden="true"></span>
      <span>Brackley Earthworks</span>
    </div>
    <div class="back-details">
      <p class="company">Brackley Earthworks</p>
      <p class="person">Name Surname</p>
      <p class="role">Position</p>
      <p class="address">14 Ridgeway Lane<br>Tallowmere Victoria 3741<br>Australia<br>Phone <strong>03 5900 1274</strong></p>
      <p class="web">admin@brackleyearthworks.com.au<br>www.brackleyearthworks.com.au</p>
    </div>
  </section>

</main>
</body>
</html>
```